RT Venture Website (professional site for investors and funds)

We want to make a website for an Holding Company that owns other companies' shares in different fields. RT is the name of the holding.
We still do not have a logo or preferred colors for the company. The company, through this website, will send a clear message: it's not important where we are, it's important what we do but more than that why we do what we do.
We search for inspiration in a simple layout because we want that the user feels comfortable and guided while exploring it. The content of the website aspire to be very impressive through one or more background images.

Below, the structure of the pages explained shortly.
To learn more, we have attached a draft of the website.

Home: page with a huge backround image that fill the whole page (maybe is better to merge the navbar with the image top color?).
About: with the same huge background image, we explain which are our fields.
Why: with the same huge background image, we explain which is our why.
Projects: dropdown list with project 1, project 2, project 3. If clicked, a box like about/why pops up in order to explain projects in detail.

Target Market(s)

Investors, Entrepreneurs

Industry/Entity Type

It Company

Number of Pages Required

4 page

Font styles to use
Sans Serif

Requirements
Must have
• An idea for the background image (color and design)
• Menu
• Page layout for about/why/projects
Nice to have
• Tips for color to use in this design
Should not have
• Complicated stuff

```html
<!DOCTYPE html>
<html lang="en">
<head>
<meta charset="UTF-8">
<title>RT Venture</title>
<link href="https://fonts.googleapis.com/css2?family=Lato:wght@400;700;900&family=Montserrat:wght@600&display=swap" rel="stylesheet">
<style>
  :root {
    --sky-top: #1d3760;
    --sky-mid: #4c6a85;
    --sunset: #e39a4a;
    --sun-core: #ffd98a;
    --skyline: #2a2a33;
    --water: #24395a;
    --water-deep: #16284a;
    --footer: rgba(24, 56, 122, 0.92);
    --white: #ffffff;
    --soft-white: rgba(255, 255, 255, 0.9);
  }
  * { margin: 0; padding: 0; box-sizing: border-box; }
  html, body {
    width: 1200px;
    height: 756px;
    overflow: hidden;
  }
  body {
    position: relative;
    font-family: "Lato", sans-serif;
    color: var(--white);
    background: var(--water-deep);
  }
  .hero-backdrop {
    position: absolute;
    inset: 0;
    background:
      radial-gradient(ellipse 260px 170px at 1010px 290px, rgba(255, 217, 138, 0.9), rgba(255, 217, 138, 0) 70%),
      radial-gradient(ellipse 520px 260px at 900px 330px, rgba(227, 154, 74, 0.65), rgba(227, 154, 74, 0) 75%),
      linear-gradient(180deg,
        var(--sky-top) 0%,
        var(--sky-mid) 16%,
        #8a7868 28%,
        var(--sunset) 40%,
        #7a5236 52%,
        var(--skyline) 60%,
        var(--water) 74%,
        var(--water-deep) 100%);
  }
  .site-header {
    position: absolute;
    top: 0; left: 0; right: 0;
    height: 110px;
  }
  .brand {
    position: absolute;
    left: 125px;
    top: 32px;
    font-family: "Montserrat", sans-serif;
    font-weight: 600;
    font-size: 35px;
    letter-spacing: 0.2px;
  }
  .main-nav {
    position: absolute;
    top: 39px;
    left: 616px;
    display: flex;
    align-items: center;
    height: 42px;
  }
  .nav-link {
    font-weight: 700;
    font-size: 17px;
    color: var(--white);
    text-decoration: none;
    text-align: center;
  }
  .nav-link.is-active {
    width: 99px;
    height: 42px;
    line-height: 38px;
    border: 2px solid var(--white);
  }
  .nav-link.about { margin-left: 47px; }
  .nav-link.why { margin-left: 71px; }
  .nav-link.projects { margin-left: 71px; }
  .hero-copy {
    position: absolute;
    left: 118px;
    top: 296px;
  }
  .hero-title {
    font-weight: 900;
    font-size: 45px;
    line-height: 50px;
    text-transform: uppercase;
    letter-spacing: 0.2px;
  }
  .hero-subtitle {
    margin: 2px 0 0 8px;
    font-weight: 700;
    font-size: 27px;
    line-height: 36px;
    text-transform: uppercase;
  }
  .hero-text {
    margin: 12px 0 0 7px;
    font-size: 16px;
    line-height: 20px;
    color: var(--soft-white);
  }
  .site-footer {
    position: absolute;
    left: 0; right: 0; bottom: 0;
    height: 63px;
    background: var(--footer);
    display: flex;
    align-items: center;
  }
  .legal {
    position: absolute;
    left: 117px;
    font-size: 13px;
    color: var(--soft-white);
    word-spacing: 1px;
  }
  .social-links {
    position: absolute;
    right: 110px;
    display: flex;
    gap: 22px;
    list-style: none;
  }
  .social-links a {
    font-weight: 700;
    font-size: 14px;
    color: var(--white);
    text-decoration: none;
  }
</style>
</head>
<body>
  <div class="hero-backdrop" role="img" aria-label="Aerial photograph of a city skyline at sunset with a suspension bridge over the river"></div>

  <header class="site-header">
    <div class="brand">RT Venture</div>
    <nav class="main-nav">
      <a class="nav-link is-active" href="#home">Home</a>
      <a class="nav-link about" href="#about">About</a>
      <a class="nav-link why" href="#why">Why</a>
      <a class="nav-link projects" href="#projects">Projects</a>
    </nav>
  </header>

  <main class="hero-copy">
    <h1 class="hero-title">Welcome to RT Venture</h1>
    <h2 class="hero-subtitle">Nam eget lacus aliquam volutpa</h2>
    <p class="hero-text">Ut nisi erat fermentum vel congue id euismod in elit Fusce<br>ultricies orci ac feugiat suscipit leo massa sodales</p>
  </main>

  <footer class="site-footer">
    <p class="legal">© 2017 Company Name&nbsp; All right reserved&nbsp; Term of Use</p>
    <ul class="social-links">
      <li><a href="#flit">Flit</a></li>
      <li><a href="#fable">Fable</a></li>
      <li><a href="#nexo">Nexo</a></li>
      <li><a href="#orbit">Orbit</a></li>
    </ul>
  </footer>
</body>
</html>
```